Blue Harbor Audio

need a business card for a dj and sound equipment hire(rentals) business based in Melbourne. i have attached a current card get an idea. card needs to be unique professional looking.

ps.this card is not for a DJ. it's a rental business of dj equipment and pa systems.

Industry/Entity Type

Business

Font styles to use
Sans Serif
Script

Requirements
Must have
• Business Name: BLUE HARBOR AUDIO
Contact Person: RAVINDU PERERA
Mobile: 047 BLAST 28
Email: RAVINDU@BLUEHARBORAUDIO.COM.AU
Website: WWW.BLUEHARBORAUDIO.COM.AU
SocialPage: WWW.SOCIALPAGE.CM/BLUEHARBORAUDIO.COM.AU

```html
<!DOCTYPE html>
<html lang="en">
<head>
<meta charset="utf-8">
<title>Blue Harbor Audio – Business Card</title>
<link rel="stylesheet" href="https://fonts.googleapis.com/css2?family=Arimo:wght@400&family=Josefin+Sans:wght@300&display=swap">
<style>
  :root {
    --canvas: #ffffff;
    --card: #231f20;
    --band: #4ac4dc;
    --ink-dark: #1e1e1e;
    --ink-light: #e6e6e6;
    --ink-white: #ffffff;
    --shadow: rgba(0, 0, 0, 0.35);
    --decor: rgba(255, 255, 255, 0.07);
  }
  * { margin: 0; padding: 0; box-sizing: border-box; }
  html, body {
    width: 1200px; height: 900px; overflow: hidden;
    background: var(--canvas);
  }
  .stage { position: relative; width: 1200px; height: 900px; }

  .card {
    position: absolute;
    width: 698px; height: 399px;
    background: var(--card);
    box-shadow: 3px 4px 4px var(--shadow);
    font-family: "Arimo", Arial, sans-serif;
    color: var(--ink-light);
    overflow: hidden;
  }
  .card--front { left: 153px; top: 17px; }
  .card--back  { left: 350px; top: 470px; }

  .wordmark {
    position: absolute;
    font-family: "Josefin Sans", "Century Gothic", sans-serif;
    font-weight: 300;
    color: var(--ink-white);
    white-space: nowrap;
    letter-spacing: 0.5px;
  }
  .card--front .wordmark { right: 32px; top: 118px; font-size: 30px; }
  .card--back  .wordmark { left: 0; right: 0; top: 170px; text-align: center; font-size: 36px; }

  .headset-decor {
    position: absolute; left: 20px; top: -20px; width: 440px; height: 400px;
    background: radial-gradient(ellipse at 50% 45%, var(--decor) 0%, transparent 70%);
  }

  .name-band {
    position: absolute; left: -3px; right: 0; top: 266px; height: 26px;
    background: var(--band);
    color: var(--ink-dark);
    font-size: 18px; line-height: 26px;
    text-align: center; letter-spacing: 0.6px;
    padding-left: 12px;
  }
  .phone {
    position: absolute; left: 0; right: 0; top: 300px;
    text-align: center; font-size: 13px; letter-spacing: 0.6px;
  }
  .contact-row {
    position: absolute; left: 0; right: 0; top: 341px;
    display: flex; justify-content: center; align-items: center;
    font-size: 13px; letter-spacing: 0.7px; white-space: nowrap;
  }
  .contact-row .divider {
    display: inline-block; width: 1px; height: 24px;
    background: var(--ink-light); margin: 0 12px;
  }
  .social {
    position: absolute; left: 0; right: 0; top: 366px;
    text-align: center; font-size: 13px; letter-spacing: 1.6px; white-space: nowrap;
  }
  .card--back .website {
    position: absolute; left: 0; right: 0; bottom: 48px;
    text-align: center; font-size: 14px; letter-spacing: 0.8px;
  }
</style>
</head>
<body>
<main class="stage">
  <section class="card card--front" aria-label="Business card front">
    <div class="headset-decor" role="img" aria-label="Faint large headphone decoration"></div>
    <p class="wordmark">BLUE HARBOR AUDIO</p>
    <p class="name-band">RAVINDU PERERA</p>
    <p class="phone">047 BLAST 28</p>
    <p class="contact-row">
      <span class="email">RAVINDU@BLUEHARBORAUDIO.COM.AU</span>
      <span class="divider"></span>
      <span class="web">WWW.BLUEHARBORAUDIO.COM.AU</span>
    </p>
    <p class="social">WWW.SOCIALPAGE.CM/BLUEHARBORAUDIO.COM.AU</p>
  </section>

  <section class="card card--back" aria-label="Business card back">
    <p class="wordmark">BLUE HARBOR AUDIO</p>
    <p class="website">WWW.BLUEHARBORAUDIO.COM.AU</p>
  </section>
</main>
</body>
</html>
```